Brochure Design Project -postcard size 1/4 of A4 sheet

We are a bright and happening cafe which is an old milk bar converted into a cafe. I need to have a postcard designed for letterbox drop to let locals know what great food and coffee we have. The postcard ideally would have a black and white old world milk bar scene and a promise of old fashion service in a changing neighborhood.
Here is a little about our place
http://www.nearbylist.com.au/business/carwell-lane-soda-shop/richmond
I can't seem to put any updates but if you are having trouble with image graphics are ok that depicts an "old world" coffee shoo from 60s or 70s postcard size is a 1/4 of an A4 sheet
http://www.friendspage.example/group.php?gid=51847260913&v=wall
I am working off an iPad and this website does not allow feedback via iPad so have to put everything in brief link to a Facebook site now
Updates
Yeyyy !! I have been working off an Ipad which does not allow me to give feedback. I love the old world look of the recent designs I have now attached our logo and a facebook site of the cafe for more details.
Many Thanks
Marl a
Target Market(s)
Local community aged mainly 20 to 50
Industry/Entity Type
Fashion
Requirements
Must have
- Black and white image on the front of postcard an old milk bar scene and the words
Carwell lane soda shop ....a constant among change
Nice to have
- On the back to read we need to know what you want at your local foodstore
A little about our milk bar can be read at

```html
<!DOCTYPE html>
<html lang="en">
<head>
<meta charset="utf-8">
<title>Carwell Lane Soda Shop – Postcard</title>
<link rel="stylesheet" href="https://fonts.googleapis.com/css2?family=Lobster&family=PT+Sans:ital,wght@0,400;0,700;1,400&family=Roboto+Condensed:wght@400;700&display=swap">
<style>
  :root {
    --page: #e9e6e1;
    --wood-light: #f8dc92;
    --wood-mid: #f1c66c;
    --wood-deep: #e8b458;
    --ink-brown: #4a2a14;
    --dot-white: rgba(255, 255, 255, 0.85);
    --scene-sky: #5f8fc7;
    --scene-deep: #3a3f7a;
    --scene-warm: #8a5a3a;
    --divider: #1a1a1a;
  }
  * { box-sizing: border-box; margin: 0; padding: 0; }
  html, body { width: 1200px; height: 900px; overflow: hidden; }
  body {
    background: var(--page);
    position: relative;
    font-family: "PT Sans", sans-serif;
  }

  .card {
    position: absolute;
    background: linear-gradient(170deg, var(--wood-light) 0%, var(--wood-mid) 55%, var(--wood-deep) 100%);
    box-shadow: 0 4px 14px rgba(0,0,0,0.25);
    overflow: hidden;
  }
  .card-frame {
    position: absolute;
    border: 5px dotted var(--dot-white);
    border-radius: 14px;
  }

  /* Brand name: set in the piece's own text font, one colour, one weight */
  .brand-name {
    font-family: "PT Sans", sans-serif;
    font-weight: 700;
    font-style: normal;
    color: var(--ink-brown);
    line-height: 1.05;
  }

  /* Front */
  .card-front { left: 40px; top: 60px; width: 470px; height: 660px; }
  .card-front .card-frame { left: 20px; top: 20px; right: 20px; bottom: 120px; }
  .card-front .brand-name {
    position: absolute; left: 40px; top: 48px; font-size: 30px; width: 240px;
  }
  .tagline {
    position: absolute; right: 34px; top: 298px;
    font-family: "Roboto Condensed", sans-serif;
    font-weight: 700; font-size: 17px; color: #fff;
  }
  .shop-scene {
    position: absolute; left: 0; right: 0; top: 330px; bottom: 0;
    border-top-right-radius: 40px;
    background: linear-gradient(180deg, var(--scene-sky) 0%, var(--scene-deep) 55%, var(--scene-warm) 100%);
  }
  .scene-ground {
    position: absolute; left: 0; right: 0; bottom: 0; height: 40px;
    background: var(--wood-mid);
    border-top: 4px solid #9ccf7a;
  }

  /* Back */
  .card-back { left: 540px; top: 250px; width: 620px; height: 460px; }
  .card-back .card-frame { left: 18px; top: 18px; right: 18px; bottom: 18px; }
  .reviews {
    position: absolute; left: 36px; top: 44px; width: 272px;
    color: var(--ink-brown);
  }
  .review { margin-bottom: 22px; }
  .review-title {
    display: flex; align-items: center; gap: 6px;
    font-family: "Lobster", cursive; font-size: 22px; font-weight: 400;
  }
  .review-title svg { flex: none; }
  .review-quote {
    font-style: italic; font-size: 13.5px; line-height: 1.22; text-align: justify;
  }
  .divider {
    position: absolute; left: 322px; top: 60px; width: 3px; height: 350px;
    background: var(--divider);
  }
  .back-brand {
    position: absolute; left: 356px; top: 62px;
    display: flex; align-items: flex-start; gap: 12px;
  }
  .back-brand .brand-name { font-size: 28px; width: 180px; }
  .brand-square {
    width: 44px; height: 44px; background: #fff;
    border: 2px solid var(--ink-brown); margin-top: 4px;
  }
  .address {
    position: absolute; left: 362px; top: 250px;
    font-family: "Roboto Condensed", sans-serif;
    font-size: 30px; line-height: 1.18; color: var(--ink-brown);
    font-style: normal;
  }
</style>
</head>
<body>

  <section class="card card-front" aria-label="Postcard front">
    <div class="card-frame"></div>
    <h1 class="brand-name">Carwell Lane Soda Shop</h1>
    <p class="tagline">...a constant amongst change</p>
    <div class="shop-scene" role="img" aria-label="Painted street view of the cafe shopfront with umbrellas and outdoor seating">
      <div class="scene-ground"></div>
    </div>
  </section>

  <section class="card card-back" aria-label="Postcard back">
    <div class="card-frame"></div>

    <div class="reviews">
      <article class="review">
        <h2 class="review-title">
          <svg width="16" height="16" viewBox="0 0 16 16"><path d="M8 0 L10 6 L16 8 L10 10 L8 16 L6 10 L0 8 L6 6 Z" fill="#fff"/></svg>
          Hip and Friendly
        </h2>
        <p class="review-quote">“There is a real charm about this place. I’ve lived nearby when it was the local milk bar, useful but not a place you’d want to stop for long. Now it’s a hip cafe.”</p>
      </article>
      <article class="review">
        <h2 class="review-title">
          <svg width="16" height="16" viewBox="0 0 16 16"><path d="M8 0 L10 6 L16 8 L10 10 L8 16 L6 10 L0 8 L6 6 Z" fill="#fff"/></svg>
          Local Secret
        </h2>
        <p class="review-quote">“This place is well known to locals but is still a bit of a secret for the rest of Hollowbrook. It also has coffee worth stopping for.”</p>
      </article>
      <article class="review">
        <h2 class="review-title">
          <svg width="16" height="16" viewBox="0 0 16 16"><path d="M8 0 L10 6 L16 8 L10 10 L8 16 L6 10 L0 8 L6 6 Z" fill="#fff"/></svg>
          Affordable
        </h2>
        <p class="review-quote">“Locals know this place well. It’s also family friendly so if you want an affordable breakfast out with your kids and friends all sitting at one big table this is a good place for you.”</p>
      </article>
    </div>

    <div class="divider"></div>

    <div class="back-brand">
      <h2 class="brand-name">Carwell Lane Soda Shop</h2>
      <div class="brand-square"></div>
    </div>

    <address class="address">
      52 Carwell Lane<br>
      Hollowbrook<br>
      VIC 3188<br>
      (03) 9555 0142
    </address>
  </section>

</body>
</html>
```